Fetch & Fling - New Shopify-based - eCommerce Dog Toy

Seeking a custom-coded, 5-page (home, about, store, street team, & contact) Shopify design for a new eCommerce venture in the dog/pet niche. Our client's product, the Fetch & Fling, will be a direct competitor to the famous Tossa-Rok ball launcher.

Color palette:
Green Gecko:13-0340TN, #69FF47
Blue: 072C, #10069F

Logos attached (additional file formats available upon request)

Please use stock dog-related photos for now. ***Will update the brief in a few days with professional photos from a recent lifestyle shoot***

Homepage wireframe here: https://app.frameloom-example.com/QZP8r4Kd7WnHbYtE2LvXcM9sJuFgA3Nq/view/page/c3e81d5f0

Target Market(s)

dog owners

Industry/Entity Type

pet / dog

Coding

Coded - Design and coding required

Font styles to use
Serif
Sans Serif

Requirements
Must have
• See wireframe
Should not have
• Please do not reference Tossa-rok directly

```html
<!DOCTYPE html>
<html lang="en">
<head>
<meta charset="utf-8">
<title>Fetch &amp; Fling — We Care About Your Pet</title>
<link rel="stylesheet" href="https://fonts.googleapis.com/css2?family=Lexend:wght@400;500;600&family=Poppins:wght@400;500;600&display=swap">
<style>
:root{
  --navy:#10069F;
  --navy-deep:#0d0585;
  --sky:#03a9ee;
  --sky-soft:#bfe6fb;
  --green:#69FF47;
  --green-mid:#4ee13a;
  --yellow:#f7e21c;
  --ink:#222;
  --muted:#555;
  --white:#fff;
  --head:"Lexend",sans-serif;
  --body:"Poppins",sans-serif;
}
*{box-sizing:border-box;margin:0;padding:0}
html,body{width:1200px;height:4535px;overflow:hidden}
body{position:relative;background:var(--white);font-family:var(--body);color:var(--ink)}
.abs{position:absolute}
.photo{position:absolute;display:block}

/* header */
.brand{position:absolute;display:flex;align-items:center;gap:8px;font-family:var(--head);font-weight:600;color:var(--navy);font-size:26px;white-space:nowrap}
.brand-dot{width:16px;height:16px;border-radius:50%;background:var(--green)}
.nav{position:absolute;top:20px;left:525px;display:flex;gap:26px;font-family:var(--head);font-weight:500;font-size:16px;color:var(--navy)}
.nav .home{width:14px;height:14px;margin-top:3px}
.cart{position:absolute;top:24px;left:1040px;display:flex;align-items:center;gap:8px;font-size:13px;font-weight:600;color:var(--navy)}
.cart-badge{position:absolute;left:0;top:16px;width:16px;height:16px;border-radius:50%;background:var(--yellow);font-size:9px;text-align:center;line-height:16px;color:var(--navy)}

/* hero */
.hero-offer{top:292px;left:88px;font-family:var(--head);color:var(--green);font-size:26px;font-weight:500}
.hero-title{top:330px;left:88px;font-family:var(--head);color:var(--white);font-size:52px;font-weight:600;line-height:1}
.btn{display:inline-block;font-family:var(--head);font-weight:600;font-size:14px;text-transform:uppercase;border-radius:24px;text-align:center;letter-spacing:.3px}
.btn-yellow{position:absolute;top:450px;left:88px;width:150px;height:48px;line-height:48px;background:var(--yellow);color:var(--navy)}
.btn-play{position:absolute;top:447px;left:240px;width:54px;height:54px;border-radius:50%;background:var(--green);border:4px solid #fff}
.btn-sky{position:absolute;width:150px;height:44px;line-height:44px;background:var(--sky);color:var(--white)}

/* content blocks */
.h2{position:absolute;font-family:var(--head);font-weight:500;color:var(--navy);font-size:44px;line-height:1.1}
.copy{position:absolute;font-size:13.5px;line-height:22px;color:#333}
.dots{position:absolute;display:flex;gap:6px}
.dots i{width:10px;height:10px;border-radius:50%;background:#ddd}
.dots i.on{background:var(--yellow)}

.feature{position:absolute;width:200px;text-align:center;font-family:var(--head);font-weight:500;font-size:19px;color:#222}
.feature svg{display:block;margin:0 auto 14px}

.eyebrow{position:absolute;font-family:var(--head);color:var(--sky);font-size:21px}

.team-title{top:2262px;left:643px;font-family:var(--head);font-weight:500;color:var(--white);font-size:44px}
.team-copy{top:2322px;left:645px;width:470px;color:var(--white)}
.arrow{position:absolute;width:38px;height:38px;border-radius:50%;font-size:16px;text-align:center;line-height:38px}

.center-title{position:absolute;left:0;width:1200px;text-align:center;font-family:var(--head);font-weight:500;color:var(--navy);font-size:44px}
.journey{position:absolute;top:3363px;width:247px;height:301px;border-radius:14px}

.review{position:absolute;top:3837px;width:420px;height:220px;background:#fff;border-radius:28px;box-shadow:0 8px 30px rgba(0,0,0,.08);padding:32px 32px}
.review .who{display:flex;align-items:center;gap:16px}
.avatar{width:68px;height:68px;border-radius:50%;background:#c9b9a8}
.name{font-family:var(--head);font-weight:600;font-size:16px;color:var(--navy)}
.stars{color:var(--yellow);font-size:17px;letter-spacing:1px}
.stars .off{color:#ddd}
.quote{position:absolute;right:40px;top:26px;font-family:Georgia,serif;font-size:110px;color:#e5e5e5;line-height:1}
.review p{margin-top:22px;font-size:13.5px;line-height:22px;color:#444}

/* footer */
.foot-links{position:absolute;top:4330px;left:405px;display:flex;gap:27px;font-family:var(--head);font-weight:500;font-size:17px;color:var(--white)}
.social{position:absolute;top:4335px;left:915px;display:flex;gap:12px;font-size:11px;font-weight:600;color:var(--white);white-space:nowrap}
.pay{position:absolute;top:4438px;left:0;width:1200px;display:flex;justify-content:center;gap:30px;font-family:var(--head);font-weight:600;font-size:15px;color:var(--white)}
.copyright{position:absolute;top:4495px;left:0;width:1200px;text-align:center;font-size:14px;color:var(--white);font-weight:500}
.to-top{position:absolute;top:4444px;left:1127px;width:42px;height:42px;border-radius:50%;background:var(--sky);color:#fff;text-align:center;line-height:42px;font-size:14px}
</style>
</head>
<body>

<svg class="abs" style="top:0;left:0" width="1200" height="4535" viewBox="0 0 1200 4535" aria-hidden="true">
  <path fill="var(--navy)" d="M0 70 C120 40 200 95 330 75 C460 55 520 70 640 68 C800 60 880 90 1000 70 C1090 55 1150 90 1200 80 L1200 760 C1130 740 1060 780 980 770 C860 755 780 680 650 650 C500 620 420 640 300 660 C180 690 90 705 0 690 Z"/>
  <path fill="none" stroke="var(--yellow)" stroke-width="7" stroke-linecap="round" d="M0 250 L185 190"/>
  <path fill="none" stroke="var(--yellow)" stroke-width="4" stroke-linecap="round" d="M40 245 L175 205"/>
  <g fill="#fff"><ellipse cx="498" cy="177" rx="17" ry="15"/><circle cx="482" cy="150" r="7"/><circle cx="500" cy="140" r="7"/><circle cx="518" cy="150" r="7"/><circle cx="528" cy="170" r="6"/></g>
  <path fill="var(--green)" opacity=".25" d="M880 1560 C980 1490 1120 1490 1200 1510 L1200 1950 L900 1950 Z"/>
  <path fill="var(--sky-soft)" d="M0 2000 C150 1950 300 1990 420 2010 C600 2040 700 2100 860 2080 C1000 2060 1100 2000 1200 1960 L1200 2200 L0 2200 Z"/>
  <path fill="var(--sky)" d="M0 1990 C160 1940 310 1995 430 2030 C600 2080 700 2130 850 2115 C1000 2100 1100 2050 1200 2150 L1200 2650 C1100 2635 1000 2660 900 2675 C760 2695 640 2660 520 2650 C400 2640 300 2670 180 2660 C100 2650 40 2630 0 2610 Z"/>
  <g fill="#fff" opacity=".8"><circle cx="540" cy="2140" r="14"/><circle cx="558" cy="2112" r="6"/><circle cx="528" cy="2110" r="6"/></g>
  <g fill="#fff" opacity=".6"><circle cx="170" cy="2535" r="18"/><circle cx="190" cy="2505" r="8"/><circle cx="160" cy="2500" r="7"/></g>
  <path fill="var(--sky)" d="M230 1320 C260 1290 320 1300 350 1330 C380 1370 360 1440 310 1455 C260 1465 205 1440 200 1395 C196 1360 210 1335 230 1320 Z"/>
  <path fill="var(--yellow)" d="M540 1305 C580 1290 650 1295 668 1340 C680 1390 660 1440 612 1455 C560 1465 530 1425 532 1380 C534 1345 520 1320 540 1305 Z"/>
  <path fill="var(--green-mid)" d="M880 1310 C930 1290 990 1310 998 1360 C1004 1410 975 1450 925 1455 C875 1460 848 1420 850 1380 C852 1345 855 1320 880 1310 Z"/>
  <path fill="var(--yellow)" d="M0 4250 C150 4210 300 4250 450 4230 C600 4210 700 4250 850 4235 C1000 4220 1100 4200 1200 4215 L1200 4300 L0 4300 Z"/>
  <path fill="var(--navy)" d="M0 4270 C160 4245 300 4285 460 4265 C620 4245 720 4285 880 4268 C1020 4252 1120 4240 1200 4250 L1200 4535 L0 4535 Z"/>
  <rect fill="var(--navy-deep)" x="0" y="4420" width="1200" height="115"/>
</svg>

<div class="brand" style="top:32px;left:88px"><span class="brand-dot"></span>Fetch &amp; Fling</div>
<nav class="nav">
  <svg class="home" viewBox="0 0 14 14" aria-hidden="true"><path fill="var(--sky)" d="M7 1 L13 7 H11 V13 H8.5 V9 H5.5 V13 H3 V7 H1 Z"/></svg>
  <span>About</span><span>Street Team</span><span>Store</span><span>Contact</span>
</nav>
<div class="cart">
  <svg width="26" height="22" viewBox="0 0 26 22" aria-hidden="true"><path fill="none" stroke="var(--navy)" stroke-width="2" d="M2 6 H24 L21 18 H5 Z M8 6 L11 1 M18 6 L15 1"/></svg>
  <span>$34.99</span><span class="cart-badge">0</span>
</div>

<div class="photo" role="img" aria-label="Corgi sniffing an orange treat toy in front of a blue circle" style="top:225px;left:500px;width:700px;height:555px;border-radius:45% 40% 30% 35%;background:radial-gradient(circle at 45% 45%,#d7924f 0%,#b9763c 40%,rgba(121,200,240,.9) 70%,rgba(16,6,159,0) 72%)"></div>
<div class="abs hero-offer">Bio-Organic 30% OFF</div>
<h1 class="abs hero-title">We Care About<br>Your Pet!</h1>
<a class="btn btn-yellow">Buy Now</a>
<span class="btn-play"><svg width="46" height="46" viewBox="0 0 46 46" aria-hidden="true"><path fill="#fff" d="M18 14 L32 23 L18 32 Z"/></svg></span>

<div class="photo" role="img" aria-label="Fluffy puppy lying between two colourful plush balls" style="top:828px;left:53px;width:555px;height:405px;border-radius:20px;background:linear-gradient(135deg,#f4f4f4,#8a5a3a 45%,#e8d66a 75%,#f4f4f4)"></div>
<h2 class="h2" style="top:895px;left:635px">Heading Here</h2>
<p class="copy" style="top:955px;left:635px;width:470px">Lorem ipsum dolor sit amet, consectetur adipiscing elit. Nulla quam velit, vulputate eu pharetra nec, mattis ac neque. Duis vulputate commodo lectus, ac blandit elit tincidunt id. Sed rhoncus, tortor sed eleifend tristique, tortor mauris molestie elit, et lacinia ipsum quam nec dui. Quisque nec mauris sit amet elit iaculis pretium sit amet quis magna. Aenean velit odio, elementum in tempus ut, vehicula eu diam. Pellentesque rhoncus aliquam mattis. Ut vulputate eros sed felis sodales nec .</p>
<a class="btn btn-sky" style="top:1151px;left:635px">Buy Now</a>
<div class="dots" style="top:1240px;left:320px"><i class="on"></i><i></i><i></i></div>

<div class="feature" style="top:1348px;left:182px">
  <svg width="80" height="70" viewBox="0 0 80 70" aria-hidden="true"><g fill="none" stroke="#fff" stroke-width="3" stroke-linejoin="round"><path d="M10 20 V45 L25 55 H35 V40 L22 30"/><path d="M70 20 V45 L55 55 H45 V40 L58 30"/></g></svg>
  <span style="position:relative;top:40px">Underhand</span></div>
<div class="feature" style="top:1348px;left:500px">
  <svg width="80" height="70" viewBox="0 0 80 70" aria-hidden="true"><g fill="none" stroke="#fff" stroke-width="3" stroke-linejoin="round"><path d="M40 5 L54 13 V29 L40 37 L26 29 V13 Z"/><path d="M10 30 V50 L25 60 H35 V47 L22 38"/><path d="M70 30 V50 L55 60 H45 V47 L58 38"/></g></svg>
  <span style="position:relative;top:40px">Overhand</span></div>
<div class="feature" style="top:1348px;left:833px">
  <svg width="80" height="70" viewBox="0 0 80 70" aria-hidden="true"><path fill="none" stroke="#fff" stroke-width="3" stroke-linejoin="round" d="M28 60 V25 M28 35 V12 H34 V34 M34 30 V8 H40 V34 M40 30 V10 H46 V34 M46 32 V16 H52 V44 C52 56 44 62 36 62 C30 62 26 58 22 52 L14 40 L18 36 L28 44"/></svg>
  <span style="position:relative;top:40px">Hands-free</span></div>

<div class="eyebrow" style="top:1595px;left:88px">About</div>
<h2 class="h2" style="top:1620px;left:88px">Fetch &amp; Fling</h2>
<p class="copy" style="top:1677px;left:88px;width:470px">Lorem ipsum dolor sit amet, consectetur adipiscing elit. Nulla quam velit, vulputate eu pharetra nec, mattis ac neque. Duis vulputate commodo lectus, ac blandit elit tincidunt id. Sed rhoncus, tortor sed eleifend tristique, tortor mauris molestie elit, et lacinia ipsum quam nec dui. Quisque nec mauris sit amet elit iaculis pretium sit amet quis magna. Aenean velit odio, elementum in tempus ut, vehicula eu diam. Pellentesque rhoncus aliquam mattis. Ut vulputate eros sed felis sodales nec .</p>
<div class="photo" role="img" aria-label="Person offering a treat to a white puppy on green grass" style="top:1548px;left:593px;width:607px;height:512px;border-radius:55% 45% 40% 60% / 45% 40% 60% 55%;background:linear-gradient(160deg,#5f87b8 0%,#3d6e9a 35%,#58a53a 55%,#7ec44e 100%)"></div>

<div class="photo" role="img" aria-label="Man in a branded t-shirt holding a pug" style="top:2110px;left:123px;width:468px;height:468px;border-radius:50%;background:radial-gradient(circle at 50% 45%,#ffffff 0%,#f0f0f0 60%,#d9d9d9 100%)"></div>
<h2 class="abs team-title">Join Our Street Team</h2>
<p class="copy team-copy">Lorem ipsum dolor sit amet, consectetur adipiscing elit. Nulla quam velit, vulputate eu pharetra nec, mattis ac neque. Duis vulputate commodo lectus, ac blandit elit tincidunt id. Sed rhoncus, tortor sed eleifend tristique, tortor mauris molestie elit, et lacinia ipsum quam nec dui. Quisque nec mauris sit amet elit iaculis pretium sit amet quis magna. Aenean velit odio, elementum in tempus ut, vehicula eu diam. Pellentesque rhoncus aliquam mattis. Ut vulputate eros sed felis sodales nec .</p>
<span class="arrow" style="top:2510px;left:645px;background:#cfe9f7;color:var(--navy)">&#8249;</span>
<span class="arrow" style="top:2510px;left:690px;background:var(--green);color:#fff">&#8250;</span>

<div class="photo" role="img" aria-label="Orange and green rubber dog toys" style="top:2605px;left:0;width:215px;height:230px;border-radius:0 50% 40% 0;background:linear-gradient(135deg,#ff7a2e 0%,#e85a1c 40%,#3a9f3a 65%,#2f7fd0 100%)"></div>
<h2 class="h2" style="top:2856px;left:92px">Heading Here</h2>
<p class="copy" style="top:2914px;left:92px;width:470px">Lorem ipsum dolor sit amet, consectetur adipiscing elit. Nulla quam velit, vulputate eu pharetra nec, mattis ac neque. Duis vulputate commodo lectus, ac blandit elit tincidunt id. Sed rhoncus, tortor sed eleifend tristique, tortor mauris molestie elit, et lacinia ipsum quam nec dui. Quisque nec mauris sit amet elit iaculis pretium sit amet quis magna. Aenean velit odio, elementum in tempus ut, vehicula eu diam. Pellentesque rhoncus aliquam mattis. Ut vulputate eros sed felis sodales nec .</p>
<a class="btn btn-sky" style="top:3110px;left:92px">Buy Now</a>
<div class="photo" role="img" aria-label="Spotted dog eating kibble beside a green treat ball" style="top:2816px;left:545px;width:600px;height:340px;border-radius:30px;background:radial-gradient(ellipse at 60% 45%,#d8d8d8 0%,#eeeeee 45%,#ffffff 75%)"></div>
<div class="dots" style="top:3200px;left:852px"><i class="on"></i><i></i><i></i></div>

<h2 class="center-title" style="top:3286px">Follow the journey</h2>
<div class="journey" role="img" aria-label="Dachshund chewing a blue ring toy" style="left:88px;background:linear-gradient(160deg,#9a6b4a,#6b3f22 55%,#2c72b8)"></div>
<div class="journey" role="img" aria-label="Woman playing fetch with a dog in a kitchen" style="left:347px;background:linear-gradient(160deg,#cfc7bd,#8c7d6f 55%,#3b3430)"></div>
<div class="journey" role="img" aria-label="Bulldog with an orange ball toy" style="left:605px;background:linear-gradient(160deg,#f4f4f4,#b98e62 55%,#f07a2a)"></div>
<div class="journey" role="img" aria-label="Fluffy puppy with a green spiky ball" style="left:862px;background:linear-gradient(160deg,#f3f3f3,#d2955a 55%,#b7e63a)"></div>

<h2 class="center-title" style="top:3750px">What others are saying</h2>
<article class="review" style="left:88px">
  <span class="quote">&ldquo;</span>
  <div class="who"><span class="avatar" role="img" aria-label="Reviewer portrait"></span><div><div class="name">Northgate Canopy</div><div class="stars">★★★★<span class="off">★</span></div></div></div>
  <p>It is a long established fact that a reader will be distracted by the readable content of a page when looking at its layout. It is a long...</p>
</article>
<article class="review" style="left:535px">
  <span class="quote">&ldquo;</span>
  <div class="who"><span class="avatar" role="img" aria-label="Reviewer portrait"></span><div><div class="name">Marlow Kent</div><div class="stars">★★★★<span class="off">★</span></div></div></div>
  <p>It is a long established fact that a reader will be distracted by the readable content of a page when looking at its layout. It is a long...</p>
</article>
<article class="review" style="left:982px">
  <span class="quote">&ldquo;</span>
  <div class="who"><span class="avatar" role="img" aria-label="Reviewer portrait"></span><div><div class="name">Oren Vale</div><div class="stars">★★★★<span class="off">★</span></div></div></div>
  <p>It is a long established fact that a reader will be distracted by the readable content of a page when looking at its layout. It is a long...</p>
</article>
<div class="dots" style="top:4089px;left:582px"><i style="background:var(--green)"></i><i></i><i></i></div>

<div class="photo" role="img" aria-label="Grey dog lying down with a pink ball" style="top:4127px;left:0;width:210px;height:150px;border-radius:0 60% 40% 0;background:linear-gradient(135deg,#6d6f78,#3d3f47 60%,#d96aa8)"></div>
<div class="brand" style="top:4328px;left:92px;color:var(--green)"><span class="brand-dot" style="background:var(--yellow)"></span>Fetch &amp; Fling</div>
<nav class="foot-links"><span>My Account</span><span>View Cart</span><span>My Wishlist</span><span>Order Status</span></nav>
<div class="social"><span>Barkbook</span><span>Yapper</span><span>Sniffle</span><span>Pawlink</span><span>Pinpup</span></div>
<div class="pay"><span>Marketa</span><span>Vantix</span><span>Spendle</span><span>Coincard</span><span>Coinlark</span><span>OrchardPay</span></div>
<p class="copyright">©Copyright 2022 | All Rights Reserved</p>
<span class="to-top">&#8963;</span>

</body>
</html>
```